'Tarovin' a financial/crypto-currency exchange in the middle east

On the card we need 1) Name 2) title 3) email address 4) phone number using the same colors and theme as the logo. On one side we just want the logo and we want the whole card to be in blue (same blue as logo) with the logo in the back being white.
Industry/Entity Type
Financial

```html
<!DOCTYPE html>
<html lang="en">
<head>
<meta charset="UTF-8">
<title>Tarovin Business Card</title>
<link href="https://fonts.googleapis.com/css2?family=Poppins:wght@400;500;600;700&display=swap" rel="stylesheet">
<style>
  :root {
    --brand-blue: #1b8fd2;
    --card-white: #ffffff;
    --white-faint: rgba(255, 255, 255, 0.12);
    --white-ring: rgba(255, 255, 255, 0.18);
    --stage: #2a2a2c;
  }
  * { margin: 0; padding: 0; box-sizing: border-box; }
  html, body {
    width: 1200px;
    height: 880px;
    overflow: hidden;
    background: var(--stage);
    font-family: "Poppins", sans-serif;
  }
  .canvas {
    position: relative;
    width: 1200px;
    height: 880px;
  }
  .card {
    position: absolute;
    left: 260px;
    width: 680px;
    height: 390px;
    border-radius: 22px;
    overflow: hidden;
  }
  .card--front { top: 30px; background: var(--brand-blue); }
  .card--back  { top: 460px; background: var(--card-white); }

  .front-decor {
    position: absolute;
    left: 0;
    top: 0;
    width: 680px;
    height: 390px;
  }
  .front-brand {
    position: absolute;
    left: 0;
    right: 0;
    top: 50%;
    transform: translate(40px, -50%);
    display: flex;
    justify-content: center;
    align-items: center;
    gap: 18px;
  }
  .front-brand__dot {
    width: 70px;
    height: 70px;
    border-radius: 50%;
    background: var(--card-white);
    flex: none;
  }
  .front-brand__name {
    font-size: 62px;
    font-weight: 600;
    color: var(--card-white);
    letter-spacing: 1px;
    line-height: 1;
  }

  .back-info {
    position: absolute;
    left: 0;
    right: 0;
    top: 118px;
    text-align: center;
    color: var(--brand-blue);
  }
  .back-info__brand {
    font-size: 44px;
    font-weight: 600;
    letter-spacing: 1px;
    line-height: 1.05;
  }
  .back-info__name {
    margin-top: 4px;
    font-size: 19px;
    font-weight: 600;
    line-height: 1.2;
  }
  .back-info__title {
    font-size: 14px;
    font-weight: 400;
    line-height: 1.2;
  }
  .back-info__contact {
    margin-top: 22px;
    font-size: 14px;
    font-weight: 400;
  }
  .back-info__label { font-weight: 700; }
</style>
</head>
<body>
  <main class="canvas">
    <section class="card card--front" aria-label="Card front">
      <svg class="front-decor" viewBox="0 0 680 390" aria-hidden="true">
        <circle cx="170" cy="250" r="235" fill="none" stroke="var(--white-ring)" stroke-width="10"/>
        <circle cx="170" cy="250" r="218" fill="var(--white-faint)"/>
      </svg>
      <div class="front-brand">
        <span class="front-brand__dot"></span>
        <span class="front-brand__name">Tarovin</span>
      </div>
    </section>

    <section class="card card--back" aria-label="Card back">
      <div class="back-info">
        <div class="back-info__brand">Tarovin</div>
        <div class="back-info__name">Laith Haddad</div>
        <div class="back-info__title">Founder</div>
        <div class="back-info__contact">
          <span class="back-info__label">P:</span> (555) 014-2273 |
          <span class="back-info__label">E:</span>hello@tarovinmail.com
        </div>
      </div>
    </section>
  </main>
</body>
</html>
```